Driving School Business card design

Hi, we are starting a new business (Driving School) and would like your help with our business card design.
We are located in Adelaide SA.
Our aim is to help young people achieve best possible results by promoting safe and stress free driving.

Name of our school is "Velmira" which means best or most favorable.

Hope there is someone out there in wonderful world of design who can think outside of square and give us recognizable/ unique business card design.

Target Market(s)

16+

Industry/Entity Type

Business

Contact Information for Business Card

Name of our business is "Velmira driver training"
Our idea is to make letter "L' in Velmira more distinct (noticeable) by different color or font, so it gets associated with learner driver.
We like combination of white, dark gray and yellow but do not limit our self to that.
Reverse side of our card would have to incorporate writing space for date and time of the next lesson.

Requirements
Must have
• Business name: Velmira driver training
• Owner/ instructor name
• Mobile no:
• Chatterloop logo
Should not have
• Anything Not associated with driving

```html
<!DOCTYPE html>
<html lang="en">
<head>
<meta charset="utf-8">
<title>Velmira Driver Training – Lesson Card</title>
<link rel="stylesheet" href="https://fonts.googleapis.com/css2?family=Lato:wght@400;700;900&display=swap">
<style>
  :root {
    --backdrop: #d9d9d7;
    --card: #262a2b;
    --card-deep: #1f2223;
    --white: #f2f2f2;
    --rule: #c9c9c9;
    --yellow: #f2b705;
  }
  * { margin: 0; padding: 0; box-sizing: border-box; }
  html, body {
    width: 1200px;
    height: 800px;
    overflow: hidden;
    background: var(--backdrop);
    font-family: "Lato", sans-serif;
  }
  .stage {
    width: 1200px;
    height: 800px;
    display: flex;
    align-items: center;
    justify-content: center;
  }
  .card {
    position: relative;
    width: 880px;
    height: 503px;
    background: linear-gradient(180deg, var(--card) 0%, var(--card-deep) 100%);
    box-shadow: 0 14px 40px rgba(0, 0, 0, 0.25);
    overflow: hidden;
  }
  .brand {
    position: absolute;
    top: 40px;
    left: 0;
    right: 0;
    text-align: center;
  }
  .brand-name {
    color: var(--white);
    font-weight: 900;
    font-size: 66px;
    letter-spacing: 0.16em;
    line-height: 1;
  }
  .brand-rule {
    position: absolute;
    top: 128px;
    left: 0;
    right: 0;
    height: 3px;
    background: var(--rule);
  }
  .tagline {
    position: absolute;
    top: 146px;
    left: 0;
    right: 0;
    text-align: center;
    color: var(--white);
    font-size: 17px;
    font-weight: 400;
    letter-spacing: 0.42em;
  }
  .next-lesson {
    position: absolute;
    top: 222px;
    left: 0;
    right: 0;
    text-align: center;
    color: var(--yellow);
    font-size: 17px;
    font-weight: 700;
    letter-spacing: 0.38em;
  }
  .lesson-fields {
    position: absolute;
    top: 282px;
    left: 180px;
    list-style: none;
  }
  .lesson-field {
    display: flex;
    align-items: center;
    gap: 20px;
    height: 36px;
    margin-bottom: 28px;
    color: var(--white);
    font-size: 17px;
    letter-spacing: 0.38em;
  }
  .lesson-icon { width: 34px; height: 34px; flex: none; }
</style>
</head>
<body>
<main class="stage">
  <section class="card" aria-label="Velmira driver training lesson card">
    <header class="brand">
      <span class="brand-name">VELMIRA</span>
    </header>
    <div class="brand-rule"></div>
    <p class="tagline">DRIVER TRAINING</p>

    <p class="next-lesson">NEXT LESSON WILL BE AT:</p>

    <ul class="lesson-fields">
      <li class="lesson-field">
        <svg class="lesson-icon" viewBox="0 0 34 34" aria-hidden="true">
          <rect x="3" y="6" width="28" height="25" rx="2" fill="none" stroke="var(--yellow)" stroke-width="2.5"/>
          <rect x="3" y="6" width="28" height="6" fill="var(--yellow)"/>
          <rect x="9" y="2" width="3" height="7" fill="var(--yellow)"/>
          <rect x="22" y="2" width="3" height="7" fill="var(--yellow)"/>
          <g fill="var(--yellow)">
            <rect x="8" y="16" width="4" height="3"/><rect x="15" y="16" width="4" height="3"/><rect x="22" y="16" width="4" height="3"/>
            <rect x="8" y="22" width="4" height="3"/><rect x="15" y="22" width="4" height="3"/><rect x="22" y="22" width="4" height="3"/>
          </g>
        </svg>
        <span>DATE OF LESSION</span>
      </li>
      <li class="lesson-field">
        <svg class="lesson-icon" viewBox="0 0 34 34" aria-hidden="true">
          <circle cx="17" cy="17" r="14" fill="none" stroke="var(--yellow)" stroke-width="3"/>
          <path d="M17 9 V17 H24" fill="none" stroke="var(--yellow)" stroke-width="2.5" stroke-linecap="round"/>
        </svg>
        <span>TIME OF LESSION</span>
      </li>
    </ul>
  </section>
</main>
</body>
</html>
```